Harlow Crest Newsletter designs

This will be a monthly newsletter that will start from Volume 1 issue 1 that will be 12 months total that will focus on trends of shipping, latest news on mailbox customers, tips and tricks in packing material properly to local recognition of local small business Highlights. Logos is attached and pictures can be used such as the store of a shipping center. must be able to customize as well.

```html
<!DOCTYPE html>
<html lang="en">
<head>
<meta charset="utf-8">
<title>Harlow Crest Newsletter</title>
<link href="https://fonts.googleapis.com/css2?family=Cinzel:wght@700&family=Roboto:wght@400;500;700&display=swap" rel="stylesheet">
<style>
:root{
  --red:#e3313a;
  --red-deep:#d42a33;
  --navy:#26318a;
  --navy-deep:#202a7c;
  --ink:#1d1d1d;
  --muted:#7a7a7a;
  --soft:#f4f4f4;
  --white:#ffffff;
  --display:'Cinzel', Georgia, serif;
  --body:'Roboto', Arial, sans-serif;
}
*{box-sizing:border-box;margin:0;padding:0}
html,body{width:1200px;height:5016px;overflow:hidden;background:var(--white)}
body{font-family:var(--body);color:var(--ink);position:relative}
.newsletter{position:relative;width:1200px;height:5016px}

/* hero */
.hero{position:absolute;left:0;top:0;width:1200px;height:865px;
  background:linear-gradient(180deg,#6fa6dc 0%,#a9cbec 30%,#d7e4ee 42%,#5d7a5a 46%,#8c96a3 55%,#6f7680 75%,#7a8a6a 92%,#d6dbe0 100%)}
.hero-brand{position:absolute;left:146px;top:62px;font-family:var(--display);font-weight:700;font-size:34px;color:var(--navy);letter-spacing:1px}
.hero-call{position:absolute;right:154px;top:50px;display:flex;align-items:center;gap:22px}
.hero-call .icon{width:62px;height:62px;border-radius:50%;background:var(--red);display:flex;align-items:center;justify-content:center}
.hero-call small{display:block;font-size:21px;color:#4a4a4a}
.hero-call strong{display:block;font-size:29px;font-weight:500;color:var(--ink);margin-top:4px}
.hero-kicker{position:absolute;left:0;width:1200px;top:258px;text-align:center;font-size:25px;font-weight:500;color:var(--red)}
.hero-title{position:absolute;left:0;width:1200px;top:290px;text-align:center;font-family:var(--display);font-weight:700;font-size:72px;color:var(--navy);letter-spacing:2px}

/* welcome */
.welcome{position:absolute;left:0;top:865px;width:1200px;height:772px;background:linear-gradient(180deg,var(--red) 0%,var(--red-deep) 100%)}
.welcome-mark{position:absolute;left:60px;top:190px;width:400px;height:390px;display:flex;align-items:center;justify-content:center;gap:18px}
.welcome-mark .dot{width:56px;height:56px;border-radius:50%;background:var(--white);flex:none}
.welcome-mark span{font-family:var(--display);font-weight:700;font-size:46px;color:var(--white);line-height:1.1}
.welcome-copy{position:absolute;left:567px;top:147px;width:570px;color:var(--white)}
.welcome-copy .kicker{font-size:21px;font-weight:500;color:var(--navy)}
.welcome-copy h2{font-family:var(--display);font-weight:700;font-size:41px;line-height:51px;margin-top:14px;letter-spacing:1px}
.welcome-copy p{font-size:20px;line-height:36px;margin-top:22px}

/* section headings */
.section-title{position:absolute;left:0;width:1200px;text-align:center;font-family:var(--display);font-weight:700;font-size:58px;letter-spacing:1px}
.r{color:var(--red)} .n{color:var(--navy)}

/* services */
.services{position:absolute;left:0;top:1637px;width:1200px;height:1184px;background:var(--white)}
.service-card{position:absolute;width:298px;height:308px;background:var(--white);box-shadow:0 4px 14px rgba(0,0,0,.12)}
.service-card .photo{height:236px}
.service-card h3{height:72px;line-height:72px;text-align:center;font-size:23px;font-weight:500;color:var(--ink)}
.btn{position:absolute;left:454px;top:985px;width:290px;height:74px;border-radius:37px;background:var(--red);color:var(--white);font-size:26px;font-weight:700;text-align:center;line-height:74px}

/* pick-up */
.pickup{position:absolute;left:0;top:2821px;width:1200px;height:409px;background:var(--soft)}
.carrier{position:absolute;top:194px;width:216px;height:121px;background:var(--white);border-radius:10px;box-shadow:0 3px 10px rgba(0,0,0,.06);display:flex;align-items:center;justify-content:center;font-size:27px;font-weight:700;color:var(--navy)}

/* news */
.news{position:absolute;left:0;top:3230px;width:1200px;height:1348px;background:var(--white)}
.news-card{position:absolute;left:189px;width:822px;height:284px;border:1px solid #e2e2e2;border-radius:6px;background:var(--white)}
.news-card .photo{position:absolute;left:12px;top:12px;width:294px;height:264px}
.news-card h3{position:absolute;left:348px;top:26px;font-size:24px;font-weight:500;color:var(--ink)}
.news-card p{position:absolute;left:348px;top:80px;width:450px;font-size:20px;line-height:33px;color:var(--muted)}
.news-card .byline{position:absolute;left:348px;top:202px;display:flex;align-items:center;gap:14px;font-size:19px;font-weight:500;color:var(--navy)}
.avatar{width:52px;height:52px;border-radius:50%;background:#c9b7a6}

/* footer */
.footer{position:absolute;left:0;top:4578px;width:1200px;height:438px;background:linear-gradient(180deg,var(--navy) 0%,var(--navy-deep) 100%);color:var(--white)}
.footer-brand{position:absolute;left:0;width:1200px;top:58px;text-align:center;font-family:var(--display);font-weight:700;font-size:40px}
.contact{position:absolute;top:202px;display:flex;align-items:center;gap:22px}
.contact .icon{width:62px;height:62px;border-radius:50%;background:var(--red);display:flex;align-items:center;justify-content:center;flex:none}
.contact div{font-size:22px;line-height:32px}
.contact b{font-weight:700;font-size:24px}
.social{position:absolute;left:156px;top:341px;display:flex;gap:12px}
.social span{width:38px;height:38px;border-radius:50%;border:2px solid var(--white)}
.copyright{position:absolute;left:604px;top:348px;font-size:22px}
</style>
</head>
<body>
<div class="newsletter">

  <header class="hero" role="img" aria-label="Aerial photo of a shipping warehouse with trucks at loading docks under a blue sky">
    <div class="hero-brand">Harlow Crest</div>
    <div class="hero-call">
      <div class="icon"><svg width="30" height="30" viewBox="0 0 24 24"><path fill="#fff" d="M6.6 10.8a15.1 15.1 0 0 0 6.6 6.6l2.2-2.2c.3-.3.7-.4 1-.2 1.1.4 2.3.6 3.6.6.6 0 1 .4 1 1V20c0 .6-.4 1-1 1A17 17 0 0 1 3 4c0-.6.4-1 1-1h3.5c.6 0 1 .4 1 1 0 1.3.2 2.5.6 3.6.1.3 0 .7-.2 1z"/></svg></div>
      <div><small>Call Us Today!</small><strong>555.014.2290</strong></div>
    </div>
    <p class="hero-kicker">FOR FAST AND FRIENDLY SERVICE, COME IN</p>
    <h1 class="hero-title">HARLOW CREST</h1>
  </header>

  <section class="welcome">
    <div class="welcome-mark"><span class="dot"></span><span>Harlow Crest</span></div>
    <div class="welcome-copy">
      <p class="kicker">WELCOME TO HARLOW CREST</p>
      <h2>YOUR MAILING &amp; BUSINESS SERVICE CENTER</h2>
      <p>Lorem ipsum dolor sit amet, consectetur adipiscing elit, sed do eiusmod tempor incididunt ut labore et dolore magna dolor in reprehenderit in voluptate velit esse cillum dolore eu fugiat aliqua.</p>
      <p>Ut enim ad minim veniam, quis nostrud exercitation ullamco laboris nisi ut aliquip ex ea commodo consequat. Duis aute irure nulla pariatur. Excepteur sint occaecat cupidatat non proident, sunt in culpa qui officia deserunt</p>
    </div>
  </section>

  <section class="services">
    <h2 class="section-title" style="top:112px"><span class="r">OUR</span> <span class="n">SERVICES</span></h2>
    <article class="service-card" style="left:113px;top:227px"><div class="photo" role="img" aria-label="Hands signing a document at a desk" style="background:linear-gradient(135deg,#d9d2c8,#8a8580)"></div><h3>Notary Public</h3></article>
    <article class="service-card" style="left:450px;top:227px"><div class="photo" role="img" aria-label="Cargo plane on a runway" style="background:linear-gradient(180deg,#9db8d2,#cfd8de 55%,#6f7a6a)"></div><h3>SwiftLine Shipping</h3></article>
    <article class="service-card" style="left:787px;top:227px"><div class="photo" role="img" aria-label="Courier holding a parcel" style="background:linear-gradient(135deg,#b9c3cc,#3f4c66 60%,#c9302c)"></div><h3>National Mail Service</h3></article>
    <article class="service-card" style="left:113px;top:588px"><div class="photo" role="img" aria-label="Worker in a warehouse with stocked shelves" style="background:linear-gradient(135deg,#c98b4a,#e6c79a 50%,#8a6a48)"></div><h3>Package Drop-Offs</h3></article>
    <article class="service-card" style="left:450px;top:588px"><div class="photo" role="img" aria-label="Office printer with people working behind" style="background:linear-gradient(135deg,#f2efea,#9a9894 60%,#3a3a3a)"></div><h3>Print &amp; Document</h3></article>
    <article class="service-card" style="left:787px;top:588px"><div class="photo" role="img" aria-label="Laptop showing an email inbox" style="background:linear-gradient(135deg,#e7eaef,#8796ad 55%,#2f3f66)"></div><h3>Digital Mailbox Rental</h3></article>
    <div class="btn">VISIT OUR SITE</div>
  </section>

  <section class="pickup">
    <h2 class="section-title" style="top:84px"><span class="r">NEXT</span> <span class="n">PICK-UP</span></h2>
    <div class="carrier" style="left:113px">SwiftLine</div>
    <div class="carrier" style="left:364px">Northway</div>
    <div class="carrier" style="left:618px">ParcelGo</div>
    <div class="carrier" style="left:869px">National Mail</div>
  </section>

  <section class="news">
    <h2 class="section-title" style="top:94px"><span class="n">LATEST</span> <span class="r">NEWS</span></h2>
    <article class="news-card" style="top:228px">
      <div class="photo" role="img" aria-label="Hands typing on a laptop with a shipping port overlay" style="background:linear-gradient(135deg,#d99a4a,#c7b6a2 50%,#3d5b73)"></div>
      <h3>Lorem ipsum dolor sit consectetur</h3>
      <p>Sed ut perspiciatis unde omnis iste natus error sit voluptatem accusantium doloremque laudantium, totam rem aperiam,</p>
      <div class="byline"><span class="avatar"></span>Alex Rowan &nbsp;|&nbsp; Aug 07,2021</div>
    </article>
    <article class="news-card" style="top:565px">
      <div class="photo" role="img" aria-label="Tall warehouse aisle with stacked boxes" style="background:linear-gradient(180deg,#d9d6d0,#a48e70 55%,#6a5a48)"></div>
      <h3>Lorem ipsum dolor sit consectetur</h3>
      <p>Sed ut perspiciatis unde omnis iste natus error sit voluptatem accusantium doloremque laudantium, totam rem aperiam,</p>
      <div class="byline"><span class="avatar"></span>Alex Rowan &nbsp;|&nbsp; Aug 07,2021</div>
    </article>
    <article class="news-card" style="top:902px">
      <div class="photo" role="img" aria-label="Aerial view of a distribution center surrounded by green fields" style="background:linear-gradient(180deg,#8fb0cf,#5e8a4e 35%,#7c8d86 60%,#4f7a3e)"></div>
      <h3>Lorem ipsum dolor sit consectetur</h3>
      <p>Sed ut perspiciatis unde omnis iste natus error sit voluptatem accusantium doloremque laudantium, totam rem aperiam,</p>
      <div class="byline"><span class="avatar"></span>Alex Rowan &nbsp;|&nbsp; Aug 07,2021</div>
    </article>
  </section>

  <footer class="footer">
    <div class="footer-brand">Harlow Crest</div>
    <div class="contact" style="left:121px">
      <span class="icon"><svg width="26" height="30" viewBox="0 0 24 24"><path fill="#fff" d="M12 2a7 7 0 0 0-7 7c0 5 7 13 7 13s7-8 7-13a7 7 0 0 0-7-7zm0 9.5A2.5 2.5 0 1 1 12 6.5a2.5 2.5 0 0 1 0 5z"/></svg></span>
      <div>1280 Alder Mill Road,<br>Fairview, NC 27000</div>
    </div>
    <div class="contact" style="left:491px">
      <span class="icon"><svg width="26" height="26" viewBox="0 0 24 24"><path fill="#fff" d="M6.6 10.8a15.1 15.1 0 0 0 6.6 6.6l2.2-2.2c.3-.3.7-.4 1-.2 1.1.4 2.3.6 3.6.6.6 0 1 .4 1 1V20c0 .6-.4 1-1 1A17 17 0 0 1 3 4c0-.6.4-1 1-1h3.5c.6 0 1 .4 1 1 0 1.3.2 2.5.6 3.6.1.3 0 .7-.2 1z"/></svg></span>
      <div><b>Phone</b><br>555.014.2290</div>
    </div>
    <div class="contact" style="left:785px">
      <span class="icon"><svg width="26" height="22" viewBox="0 0 24 20"><path fill="#fff" d="M2 2h20v16H2z"/><path fill="none" stroke="#e3313a" stroke-width="2" d="M2 3l10 8 10-8"/></svg></span>
      <div><b>Email</b><br>info@harlowcrest.example</div>
    </div>
    <div class="social" aria-label="Social links"><span></span><span></span><span></span><span></span></div>
    <p class="copyright">Copyright © 2021 Harlow Crest - All Rights Reserved.</p>
  </footer>

</div>
</body>
</html>
```